PowerPoint Design Project

We would like 2 versions of a powerpoint presentation design that we will use to present our company to our customers.
The first version will be for our Automotive Customers
The second design will be for our other Customers.

Our company does plastic injection and assembly of plastic parts, usually as a sub contractor of our customers.

These presentations should look professional, one with a look more towards the automotive industry and the other one more towards other market than automotive.

The presentation should be easy to modify by us.

Just to clarify - what I need is a template design that fit with our brand image that should look like what's on this website - http://vardelux-demo.test/~vardelux/web/app.php/fr/produits/automobile still under construction.

                                   

 

Target Market(s)

Buyers from Big Corporations

Industry/Entity Type

Contractor

Requirements
Must have
• The look of the presentation should follow the look of our new website (still unde construction)
http://vardelux-demo.test/~vardelux/web/app.php/fr/produits/automobile

The content can be aken from the presentation attached and from our existing website
Should not have
• the turquoise logo VDX

```html
<!DOCTYPE html>
<html lang="en">
<head>
<meta charset="utf-8">
<title>Vardelux – Presentation Template</title>
<link href="https://fonts.googleapis.com/css2?family=Arimo:wght@400;700&family=Tinos:ital@1&display=swap" rel="stylesheet">
<style>
  :root {
    --canvas: #e2e2e2;
    --red: #e8141b;
    --ink: #1e1e1e;
    --body: #444;
    --muted: #8a8a8a;
    --rule: #c9c9c9;
    --slide-top: #ffffff;
    --slide-bottom: #efefef;
  }
  * { margin: 0; padding: 0; box-sizing: border-box; }
  html, body { width: 1200px; height: 797px; overflow: hidden; }
  body {
    background: var(--canvas);
    font-family: "Arimo", Arial, sans-serif;
    position: relative;
  }
  .slide {
    position: absolute;
    width: 380px; height: 302px;
    overflow: hidden;
    background: linear-gradient(160deg, var(--slide-top) 0%, #f6f6f6 45%, var(--slide-bottom) 100%);
    box-shadow: 0 1px 3px rgba(0,0,0,.25);
  }
  .slide > * { position: absolute; }
  .decor { left: 0; top: 0; width: 380px; height: 302px; }
  .decor path { fill: var(--red); }

  .slide-title { left: 73px; top: 11px; font-size: 16px; color: var(--red); line-height: 1; }
  .slide-subtitle { left: 73px; top: 29px; font-size: 11.5px; color: var(--ink); line-height: 1; }
  .title-rule { left: 73px; top: 43px; width: 280px; height: 1px; background: var(--rule); }
  .page-number { left: 10px; top: 279px; font-size: 13px; color: #fff; }

  .wordmark {
    right: 9px; bottom: 8px;
    display: flex; align-items: center; gap: 4px;
    font-size: 11px; font-weight: 700; color: var(--ink); letter-spacing: .2px;
  }
  .wordmark .mark { width: 9px; height: 9px; background: var(--red); }

  .heading { font-size: 11.5px; color: var(--red); line-height: 1; }
  .copy { font-size: 8.6px; line-height: 1.33; color: var(--body); text-align: justify; }
  .intro { font-size: 8.6px; line-height: 1.35; color: var(--body); }

  .photo { border: 1px solid #d0d0d0; box-shadow: 0 1px 2px rgba(0,0,0,.15); }
  .photo.cream { background: linear-gradient(135deg, #fbf8d8, #f1ecc0); }
  .photo.grey { background: linear-gradient(135deg, #cfcfcf, #a9a9a9); }
  .photo.orange { background: linear-gradient(135deg, #f0a524, #e08a10); }
  .photo.light { background: linear-gradient(135deg, #f4f4f4, #e0e0e0); }
  .photo.sage { background: linear-gradient(135deg, #9aa39a, #7e877f); }

  .caption { font-size: 11.5px; color: var(--red); text-align: center; line-height: 1; }

  .bullets { left: 26px; top: 107px; list-style: none; }
  .bullets li { font-size: 8.6px; color: var(--body); height: 25px; display: flex; align-items: flex-start; gap: 3px; }
  .bullets .chev { color: var(--red); font-weight: 700; font-size: 10px; line-height: .9; letter-spacing: -2px; margin-right: 2px; }

  .divider { width: 1px; background: var(--rule); }

  .cover-title { left: 18px; top: 27px; font-size: 26px; color: #111; line-height: 1; }
  .cover-subtitle { left: 18px; top: 57px; font-size: 15.5px; color: #555; line-height: 1; }

  .seal {
    width: 152px; height: 152px; border-radius: 50%;
    background: radial-gradient(circle at 50% 35%, #ffffff 0%, #f2f2f2 60%, #dcdcdc 100%);
    border: 1px solid #cfcfcf;
    box-shadow: 0 2px 5px rgba(0,0,0,.18);
    display: flex; flex-direction: column; align-items: center; justify-content: center;
    text-align: center;
  }
  .seal .group { font-size: 9.5px; color: var(--muted); line-height: 1.25; }
  .seal .name {
    display: flex; align-items: center; gap: 5px;
    margin: 10px 0 10px;
    font-size: 17px; font-weight: 700; color: var(--ink); letter-spacing: .3px;
  }
  .seal .name .mark { width: 13px; height: 13px; background: var(--red); }
  .seal .tagline { font-size: 9.5px; color: var(--muted); line-height: 1.25; }

  .thanks { left: 0; width: 380px; top: 45px; text-align: center; font-family: "Tinos", Georgia, serif; font-style: italic; font-size: 50px; color: var(--red); }
</style>
</head>
<body>

<!-- Cover -->
<section class="slide slide-cover" style="left:19px; top:67px;">
  <svg class="decor" viewBox="0 0 380 302" aria-hidden="true">
    <path d="M380 58 C250 80 140 165 88 302 H114 C168 188 262 104 380 83 Z"/>
  </svg>
  <h1 class="cover-title">Click to add Title</h1>
  <p class="cover-subtitle">Click to add subtitle</p>
  <div class="seal" style="left:208px; top:127px;">
    <span class="group">Groupe<br>Vardelux</span>
    <span class="name"><span class="mark"></span>VARDELUX</span>
    <span class="tagline">Partenaire Industriel<br>Plasturgiste</span>
  </div>
</section>

<!-- Slide 2: two headings with photos -->
<section class="slide" style="left:413px; top:67px;">
  <svg class="decor" viewBox="0 0 380 302" aria-hidden="true">
    <path d="M0 0 H88 C55 10 22 26 0 48 Z"/>
    <path d="M0 256 C18 280 42 295 66 302 H0 Z"/>
  </svg>
  <h2 class="slide-title">Enter your title here</h2>
  <p class="slide-subtitle">Enter your subtitle here</p>
  <div class="title-rule"></div>
  <h3 class="heading" style="left:12px; top:61px;">Heading 1</h3>
  <p class="copy" style="left:12px; top:74px; width:186px;">Lorem ipsum dolor sit amet, consectetur adipisicing elit,sed do eiusmod.Lorem ipsum dolor sit amet, consectetur adipisicing elit,sed do eiusmod.Lorem ipsum dolor sit amet, consectetur adipisicing elit,sed do eiusmod.</p>
  <div class="photo cream" style="left:208px; top:63px; width:150px; height:94px;" role="img" aria-label="Product photo: black moulded plastic connector part"></div>
  <h3 class="heading" style="left:10px; top:161px;">Heading 2</h3>
  <p class="copy" style="left:10px; top:174px; width:186px;">Lorem ipsum dolor sit amet, consectetur adipisicing elit,sed do eiusmod.Lorem ipsum dolor sit amet, consectetur adipisicing elit,sed do eiusmod.Lorem ipsum dolor sit amet, consectetur adipisicing elit,sed do eiusmod.</p>
  <div class="photo grey" style="left:208px; top:166px; width:150px; height:92px;" role="img" aria-label="Product photo: dark red injected plastic housing"></div>
  <span class="page-number">2</span>
  <div class="wordmark"><span class="mark"></span>VARDELUX</div>
</section>

<!-- Slide 5: bullet list -->
<section class="slide" style="left:807px; top:67px;">
  <svg class="decor" viewBox="0 0 380 302" aria-hidden="true">
    <path d="M0 0 H88 C55 10 22 26 0 48 Z"/>
    <path d="M0 256 C18 280 42 295 66 302 H0 Z"/>
  </svg>
  <h2 class="slide-title">Enter your title here</h2>
  <p class="slide-subtitle">Enter your subtitle here</p>
  <div class="title-rule"></div>
  <p class="intro" style="left:18px; top:52px; width:330px;">Lorem ipsum dolor sit amet, consectetur adipisicing elit,sed do eiusmod.Lorem ipsum dolor sit amet, consectetur adipisicing elit,sed do eiusmod.</p>
  <ul class="bullets">
    <li><span class="chev">››</span>Lorem ipsum dolor sit amet, consectetur adipisicing elit,sed do eiusmod.</li>
    <li><span class="chev">››</span>Lorem ipsum dolor sit amet, consectetur adipisicing elit,sed do eiusmod.</li>
    <li><span class="chev">››</span>Lorem ipsum dolor sit amet, consectetur adipisicing elit,sed do eiusmod.</li>
    <li><span class="chev">››</span>Lorem ipsum dolor sit amet, consectetur adipisicing elit,sed do eiusmod.</li>
    <li><span class="chev">››</span>Lorem ipsum dolor sit amet, consectetur adipisicing elit,sed do eiusmod.</li>
  </ul>
  <span class="page-number">5</span>
  <div class="wordmark"><span class="mark"></span>VARDELUX</div>
</section>

<!-- Slide 8: product grid -->
<section class="slide" style="left:19px; top:435px;">
  <svg class="decor" viewBox="0 0 380 302" aria-hidden="true">
    <path d="M0 0 H88 C55 10 22 26 0 48 Z"/>
    <path d="M0 256 C18 280 42 295 66 302 H0 Z"/>
  </svg>
  <h2 class="slide-title">Enter your title here</h2>
  <p class="slide-subtitle">Enter your subtitle here</p>
  <div class="title-rule"></div>
  <p class="intro" style="left:18px; top:50px; width:315px;">Lorem ipsum dolor sit amet, consectetur adipisicing elit,sed do eiusmod.Lorem ipsum dolor sit amet, consectetur adipisicing elit,sed do eiusmod.</p>
  <div class="photo orange" style="left:19px; top:92px; width:98px; height:67px;" role="img" aria-label="Product photo: blue diving mask"></div>
  <div class="photo light" style="left:128px; top:92px; width:106px; height:67px;" role="img" aria-label="Product photo: black plastic handle part"></div>
  <div class="photo light" style="left:247px; top:92px; width:107px; height:67px;" role="img" aria-label="Product photo: black plastic tube connector"></div>
  <span class="caption" style="left:19px; top:162px; width:98px;">Heading 1</span>
  <span class="caption" style="left:128px; top:162px; width:106px;">Heading 2</span>
  <span class="caption" style="left:247px; top:162px; width:107px;">Heading 3</span>
  <div class="photo sage" style="left:21px; top:182px; width:96px; height:72px;" role="img" aria-label="Product photo: green and white plastic cartridge"></div>
  <div class="photo light" style="left:127px; top:182px; width:108px; height:72px;" role="img" aria-label="Product photo: black plastic funnel assembly"></div>
  <div class="photo light" style="left:253px; top:182px; width:90px; height:72px;" role="img" aria-label="Product photo: black screw cap with red marking"></div>
  <span class="caption" style="left:21px; top:256px; width:96px;">Heading 4</span>
  <span class="caption" style="left:127px; top:256px; width:108px;">Heading 5</span>
  <span class="caption" style="left:253px; top:256px; width:90px;">Heading 6</span>
  <span class="page-number">8</span>
  <div class="wordmark"><span class="mark"></span>VARDELUX</div>
</section>

<!-- Slide 10: two columns -->
<section class="slide" style="left:413px; top:435px;">
  <svg class="decor" viewBox="0 0 380 302" aria-hidden="true">
    <path d="M0 0 H88 C55 10 22 26 0 48 Z"/>
    <path d="M0 256 C18 280 42 295 66 302 H0 Z"/>
  </svg>
  <h2 class="slide-title">Enter your title here</h2>
  <p class="slide-subtitle">Enter your subtitle here</p>
  <div class="title-rule"></div>
  <h3 class="heading" style="left:19px; top:65px;">Heading 1</h3>
  <div class="photo orange" style="left:18px; top:83px; width:138px; height:76px;" role="img" aria-label="Product photo: blue diving mask"></div>
  <p class="copy" style="left:18px; top:164px; width:139px;">Lorem ipsum dolor sit amet, consectetur adipisicing elit,sed do eiusmod.Lorem ipsum dolor sit amet, consectetur adipisicing elit,sed do eiusmod.Lorem ipsum dolor sit amet, consectetur .</p>
  <div class="divider" style="left:174px; top:70px; height:180px;"></div>
  <h3 class="heading" style="left:200px; top:64px;">Heading 2</h3>
  <div class="photo cream" style="left:195px; top:83px; width:160px; height:74px;" role="img" aria-label="Product photo: black moulded plastic connector part"></div>
  <p class="copy" style="left:196px; top:163px; width:161px;">Lorem ipsum dolor sit amet, consectetur adipisicing elit,sed do eiusmod. Lorem ipsum dolor sit amet, consectetur adipisicing elit,sed do eiusmod.Lorem ipsum dolor sit amet, consectetur .</p>
  <span class="page-number">10</span>
  <div class="wordmark"><span class="mark"></span>VARDELUX</div>
</section>

<!-- Slide 11: closing -->
<section class="slide" style="left:807px; top:435px;">
  <svg class="decor" viewBox="0 0 380 302" aria-hidden="true">
    <path d="M0 0 H88 C55 10 22 26 0 48 Z"/>
    <path d="M0 256 C18 280 42 295 66 302 H0 Z"/>
  </svg>
  <p class="thanks">Thank you !</p>
  <div class="seal" style="left:123px; top:134px;">
    <span class="group">Groupe<br>Vardelux</span>
    <span class="name"><span class="mark"></span>VARDELUX</span>
    <span class="tagline">Partenaire Industriel<br>Plasturgiste</span>
  </div>
  <span class="page-number">11</span>
</section>

</body>
</html>
```